Business Card Revision

Need to redesign my business cards for a new professional look. We are a courier company. You can go to www.qvrunners.com to see what we do. The trucks have an old company name (Sprout) on them but that is the company we are just now
changing the name.

Target Market(s)

Potential clients. We service the automotive, plumbing, printing, air freight industries as well as many others.

Industry/Entity Type

Business

Contact Information for Business Card

QVmotion
20864 Lark Fenmore Parkway
Havenport, Oh 45873

Thomas R. Wendall
President

tom@qvrunners.com

Main: (555) 555-0147

```html
<!DOCTYPE html>
<html lang="en">
<head>
<meta charset="utf-8">
<title>QV Runners – Business Card</title>
<link rel="stylesheet" href="https://fonts.googleapis.com/css2?family=Arimo:wght@400;700&display=swap">
<style>
  :root {
    --ink: #0b0b0b;
    --green: #3bb54a;
    --blue: #1f7cc4;
    --white: #ffffff;
    --text: #1a1a1a;
    --rule: #555555;
    --page: #e9e6e1;
  }
  html, body {
    margin: 0;
    width: 1200px;
    height: 900px;
    overflow: hidden;
    background: var(--page);
    font-family: "Arimo", Arial, sans-serif;
  }
  .card {
    position: absolute;
    left: 75px;
    top: 150px;
    width: 1050px;
    height: 600px;
    background: var(--white);
    box-shadow: 0 10px 30px rgba(0,0,0,0.18);
    overflow: hidden;
  }
  .card-shapes {
    position: absolute;
    inset: 0;
  }
  .brand-name {
    position: absolute;
    left: 450px;
    top: 72px;
    margin: 0;
    font-size: 72px;
    font-weight: 700;
    letter-spacing: 2px;
    color: var(--green);
    line-height: 1;
    white-space: nowrap;
  }
  .person {
    position: absolute;
    left: 250px;
    top: 318px;
    width: 340px;
  }
  .person-name {
    margin: 0;
    font-size: 33px;
    font-weight: 700;
    color: var(--text);
    white-space: nowrap;
  }
  .person-title {
    margin: 8px 0 0;
    font-size: 25px;
    color: var(--blue);
  }
  .divider {
    position: absolute;
    left: 615px;
    top: 272px;
    width: 2px;
    height: 165px;
    background: var(--rule);
  }
  .contact {
    position: absolute;
    left: 640px;
    top: 264px;
    margin: 0;
    font-style: normal;
    font-size: 25px;
    line-height: 36px;
    color: var(--text);
    white-space: nowrap;
  }
  .contact-line {
    display: flex;
    align-items: center;
    gap: 10px;
  }
  .contact-icon {
    width: 20px;
    height: 20px;
    flex: none;
  }
  .website {
    position: absolute;
    left: 250px;
    top: 528px;
    margin: 0;
    font-size: 26px;
    font-weight: 700;
    line-height: 1;
    color: var(--white);
    letter-spacing: 0.5px;
  }
</style>
</head>
<body>
  <div class="card">
    <svg class="card-shapes" width="1050" height="600" viewBox="0 0 1050 600" aria-hidden="true">
      <rect x="0" y="0" width="400" height="232" fill="var(--green)"/>
      <polygon points="0,100 200,190 400,100 400,145 200,235 0,145" fill="var(--white)"/>
      <polygon points="0,0 1050,0 1050,218 400,218 400,100 200,190 0,100" fill="var(--ink)"/>
      <rect x="0" y="232" width="1050" height="8" fill="var(--ink)"/>
      <rect x="0" y="466" width="1050" height="8" fill="var(--green)"/>
      <rect x="0" y="488" width="190" height="112" fill="var(--green)"/>
      <polygon points="160,488 210,544 160,600 190,600 240,544 190,488" fill="var(--white)"/>
      <polygon points="190,488 1050,488 1050,600 190,600 240,544" fill="var(--blue)"/>
    </svg>

    <p class="brand-name">QV RUNNERS</p>

    <div class="person">
      <p class="person-name">Thomas R. Wendall</p>
      <p class="person-title">President</p>
    </div>

    <div class="divider"></div>

    <address class="contact">
      <div>20864 Lark Fenmore Parkway</div>
      <div>Havenport, Oh 45873</div>
      <div class="contact-line">
        <svg class="contact-icon" viewBox="0 0 20 20" aria-hidden="true">
          <rect x="1" y="1" width="18" height="18" rx="3" fill="var(--blue)"/>
          <path d="M6 5c-1 1-1 3 1 6s4 4 6 4l1.5-1.5-2.5-2-1.2 1c-1-.5-2.3-1.8-2.8-2.8l1-1.2-2-2.5z" fill="var(--white)"/>
        </svg>
        <span>(555) 555-0147</span>
      </div>
      <div class="contact-line">
        <svg class="contact-icon" viewBox="0 0 20 20" aria-hidden="true">
          <rect x="1" y="1" width="18" height="18" rx="3" fill="var(--blue)"/>
          <rect x="4" y="6" width="12" height="8" fill="var(--white)"/>
          <path d="M4 6l6 5 6-5" fill="none" stroke="var(--blue)" stroke-width="1.4"/>
        </svg>
        <span>tom@qvrunners.com</span>
      </div>
    </address>

    <p class="website">www.qvrunners.com</p>
  </div>
</body>
</html>
```